Flyer Needed to Advertise New Online Reading Programs

ABOUT THE TRUST OF READING DEVELOPMENT
The Trust teaches summer reading skills programs for elementary school students, in programs offered through partnerships with universities, colleges and municipalities nationwide. The goal of each program is to build reading skills, and to foster a lifetime love of books and reading.

AIMS & TARGET MARKET
The Trust has developed a new format of its’ online reading program for elementary students, which includes live small-group video classes taught by a professional reading teacher. The Trust seeks a new graphic design for a flyer to advertise the new online reading program. The flyer will be sent to elementary schools, passed out by teachers, and then taken home by students to show parents; therefore, the primary audience for the flyer will be teachers and parents of elementary school students.

Live classes for children are completely new in online education, unlike anything else in the marketplace, and parents and teachers therefore have no experience with them. The successful design will include illustrations or photographs that allow visitors to immediately grasp/understand the new video class format, without relying heavily on a written description. Additionally, the successful flyer concept will make the program, and the video classes in particular, feel fun and appealing to kids and parents.

Below is additional information about the new live small-group video class format, which meets weekly for 6 weeks:
o During video classes, students participate from home.
o During discussions, the student’s computer (or tablet) screen is filled with live video frames of the teacher and the other students. The video frame for the teacher is larger, and the other students appear in smaller frames.
o During other video class instruction, the teacher uses a presentation screen to display pages of a book or a “whiteboard” used for instructional activities.

Notes: The flyer design could include an illustrated or photo screenshot of a video class, with children looking engaged and a teacher leading them in discussion (stock photos are okay to use in flyer design). We have included a screen shot of one of these classes for reference, but do not feel constrained to represent this screen realistically (as shown here). Layout, look and feel can be changed. Alternatively, you may choose to use a graphic other than a screenshot to bring across the concept of the video classes.

COPY AND SPECIFICATIONS
The flyer design will be one-sided and the dimensions are 8.5” x 11” in either portrait or landscape orientation. We will consider designs in color or black and white. Since we brand our flyers with logos of the universities we partner with throughout the nation, we’ll need to include a partner logo in the design. Exact copy will be provided, but layout is flexible. Screenshots from our sample classes are included to show screen layout. Stock photos are okay to use in flyer designs.

Reason: We'd like to make edits to existing designs.

Hi designers, We wanted to share our thoughts on the main image of the flyer. We're leaning towards an image that shows a sole student on a computer with the computer screen in view. The computer screen could have the sample image we provided to show how the video classes operate. Thanks! The Trust of Reading Development

Graphic Design

```html
<!DOCTYPE html>
<html lang="en">
<head>
<meta charset="utf-8">
<title>Reading Skills Classes Online this Summer</title>
<link href="https://fonts.googleapis.com/css2?family=Open+Sans:wght@300;400;600;700&display=swap" rel="stylesheet">
<style>
  :root {
    --ink: #333a40;
    --navy: #1f3f66;
    --band: #dde6ee;
    --accent: #3b7cc0;
    --white: #ffffff;
    --photo-shade: #5d6b78;
    --photo-light: #e9e7e2;
    --photo-warm: #d9734a;
    --muted: #8a9096;
  }
  * { margin: 0; padding: 0; box-sizing: border-box; }
  html, body { width: 849px; height: 1200px; overflow: hidden; background: var(--white); }
  body { font-family: "Open Sans", Arial, sans-serif; color: var(--ink); position: relative; }

  .hero { position: absolute; left: 0; top: 0; width: 849px; height: 482px; overflow: hidden; }
  .hero-photo {
    position: absolute; inset: 0;
    background:
      radial-gradient(ellipse 260px 200px at 700px 300px, rgba(217,115,74,0.55), rgba(217,115,74,0) 70%),
      radial-gradient(ellipse 420px 260px at 560px 170px, var(--photo-light), rgba(233,231,226,0) 75%),
      linear-gradient(200deg, #cfd3d6 0%, #9ea8b0 45%, var(--photo-shade) 100%);
  }
  .hero-photo::after {
    content: ""; position: absolute; left: 0; right: 0; bottom: 0; height: 190px;
    background: linear-gradient(0deg, rgba(40,52,64,0.55), rgba(40,52,64,0));
  }
  .hero-title {
    position: absolute; left: 0; top: 22px; width: 849px; text-align: center;
    font-weight: 300; font-size: 31px; line-height: 1.2; color: var(--white);
    text-shadow: 0 1px 3px rgba(0,0,0,0.35);
  }
  .hero-title strong { font-weight: 700; }
  .hero-points {
    position: absolute; left: 40px; top: 362px; list-style: none;
    color: var(--white); font-size: 16px; font-weight: 400; line-height: 1.5;
    text-shadow: 0 1px 2px rgba(0,0,0,0.35);
  }
  .hero-points li::before { content: "\2022"; margin-right: 10px; }

  .skills-band {
    position: absolute; left: 0; top: 482px; width: 849px; height: 46px;
    background: var(--band); display: flex; align-items: center; justify-content: center;
    font-size: 18px; font-weight: 400; color: var(--navy);
  }

  .section-title {
    position: absolute; left: 0; top: 548px; width: 849px; text-align: center;
    font-size: 17px; font-weight: 700; color: var(--navy); letter-spacing: 0.5px;
  }

  .column { position: absolute; top: 590px; font-size: 12px; line-height: 1.42; }
  .column-left { left: 40px; width: 380px; }
  .column-right { left: 450px; width: 385px; }
  .program { margin-bottom: 16px; }
  .program h3 { font-size: 12px; font-weight: 700; color: var(--ink); }

  .contact-box {
    position: absolute; left: 555px; top: 900px; width: 280px; height: 124px;
    background: var(--accent); color: var(--white);
    padding: 16px 16px 0 34px; font-size: 11.5px; font-weight: 700; line-height: 1.38;
  }

  .footer {
    position: absolute; left: 0; top: 1122px; width: 849px; height: 50px;
    display: flex; align-items: center; justify-content: space-around; padding: 0 40px;
  }
  .partner { font-size: 15px; font-weight: 600; color: var(--muted); display: flex; align-items: center; gap: 8px; }
  .partner-mark { width: 12px; height: 12px; background: var(--muted); }
  .partner-uni { background: var(--ink); color: var(--white); padding: 8px 14px; font-size: 14px; font-weight: 700; letter-spacing: 1px; }
</style>
</head>
<body>
  <section class="hero">
    <div class="hero-photo" role="img" aria-label="Photo placeholder: a child at a desk with books, taking part in a live small-group video reading class on a laptop, the teacher shown large on screen and classmates in smaller frames"></div>
    <h1 class="hero-title">Reading Skills Classes Online this<br><strong>Summer!</strong></h1>
    <ul class="hero-points">
      <li>Small class size</li>
      <li>A Skilled &amp; Encouraging Teacher</li>
      <li>Individualized Skills Instruction</li>
      <li>A Program of Independent Reading in Great Books</li>
    </ul>
  </section>

  <div class="skills-band">Phonics Comprehension | Fluency | Study Skills | Speed Reading | Love of Reading</div>

  <h2 class="section-title">PROGRAM DESCRIPTIONS:</h2>

  <div class="column column-left">
    <div class="program"><h3>Program for Preschoolers:</h3>
      <p>Students in this program build strong reading readiness skills. Your child will learn letter recognition and beginning phonics, and develop the motivation and love of reading that make learning to read easy, enjoyable and successful.</p></div>
    <div class="program"><h3>Program for Entering Kindergartners:</h3>
      <p>Students in this program learn beginning reading skills and develop a love of books. Your child will learn letter recognition, phonics, and sight words, and will learn to sound out short words.</p></div>
    <div class="program"><h3>Program for Entering 1st Graders:</h3>
      <p>Students in this program learn to read independently. Your child will learn phonics and sight words, build comprehension, and gain the skills and confidence needed for success in first grade.</p></div>
    <div class="program"><h3>Program for Entering 2nd Graders:</h3>
      <p>Students in this program become fluent, independent readers. Your child will make significant gains in phonics and word-attack skills, fluency, and comprehension, and will develop confidence and a love of reading.</p></div>
    <div class="program"><h3>Program for Entering 3rd Graders:</h3>
      <p>Students in this program become strong independent readers. Your child will develop the comprehension, fluency, and long-word decoding skills needed to read longer books with ease, and will build confidence and a love of reading.</p></div>
  </div>

  <div class="column column-right">
    <div class="program"><h3>Program for Entering 4th and 5th Graders:</h3>
      <p>Students in this program make substantial gains in comprehension, long-word decoding skills, fluency, and reading speed. Your child will complete homework more quickly and easily, be more successful in school, and become a strong, enthusiastic reader.</p></div>
    <div class="program"><h3>Programs for Entering 6th-8th Graders and Entering 9th and 10th Graders:</h3>
      <p>Students in these programs make substantial gains in comprehension while doubling reading speed. They also learn the best way to read textbooks, take notes, and study for tests. As a result, students complete homework more quickly and easily, get better grades, and enjoy reading more.</p></div>
  </div>

  <aside class="contact-box">
    For More Information or to Register<br>
    Call 1-800-555-0142<br>
    Mon.-Fri. 5am–7pm, Sat. 5am–6pm<br>
    and Sun. 6am–6pm<br>
    Please see reverse side for<br>
    program schedule.
  </aside>

  <footer class="footer">
    <span class="partner"><span class="partner-mark"></span>Quillmark</span>
    <span class="partner">Kestrel Learning</span>
    <span class="partner-uni">WESTBROOK UNIVERSITY</span>
    <span class="partner">Harbor Grove</span>
    <span class="partner"><span class="partner-mark"></span>Quillmark</span>
  </footer>
</body>
</html>
```